Now Leasing Banner

Looking for a banner that says the following information approx 4' x 30'

Now Leasing Maple Ridge Court 925-318-6042

Target Market(s)

Drive by traffic

Industry/Entity Type

Residential property management

Requirements
Must have
• Clear and readable from a distance

```html
<!DOCTYPE html>
<html lang="en">
<head>
<meta charset="utf-8">
<title>Now Leasing – Maple Ridge Court</title>
<link href="https://fonts.googleapis.com/css2?family=Anton&display=swap" rel="stylesheet">
<style>
  :root {
    --banner-blue: #176ba0;
    --banner-haze: #6a83a0;
    --banner-grey: #9a9a9e;
    --text-white: #ffffff;
  }
  html, body {
    margin: 0;
    padding: 0;
    width: 1200px;
    height: 160px;
    overflow: hidden;
  }
  .leasing-banner {
    position: relative;
    width: 1200px;
    height: 160px;
    background:
      linear-gradient(to right, rgba(23,107,160,0) 0%, rgba(23,107,160,0) 45%, rgba(23,107,160,0.45) 100%),
      linear-gradient(to bottom, var(--banner-blue) 0%, var(--banner-blue) 58%, var(--banner-haze) 80%, var(--banner-grey) 100%);
  }
  .banner-type {
    position: absolute;
    inset: 0;
    width: 1200px;
    height: 160px;
  }
  .banner-type text {
    font-family: "Anton", "Oswald", sans-serif;
    fill: var(--text-white);
    text-transform: uppercase;
  }
  .headline-lead { font-size: 64px; }
  .headline-main { font-size: 132px; }
  .contact-phone { font-size: 38px; }
</style>
</head>
<body>
  <div class="leasing-banner">
    <svg class="banner-type" viewBox="0 0 1200 160" xmlns="http://www.w3.org/2000/svg">
      <text class="headline-lead" x="35" y="102" textLength="88" lengthAdjust="spacingAndGlyphs">Now</text>
      <text class="headline-main" x="143" y="127" textLength="868" lengthAdjust="spacingAndGlyphs">Leasing Maple Ridge Court</text>
      <text class="contact-phone" x="1027" y="93" textLength="141" lengthAdjust="spacingAndGlyphs">925-318-6042</text>
    </svg>
  </div>
</body>
</html>
```